Advertisement Coaching practice

I need an advertisement (to be printed in newspaper). I have a coaching practice where I offer coaching, workshops family constellations and relationship therapy. The ad needs to express calmness, inspiration to transform but also not dull and boring. It would be great if you could use the colors from my logo into the ad.

Dimensions are: 13,04 cm Width x 9,72 cm Height.

I will add my previous self-made ad, my company logo, a portrait photo of myself and the text I want to add. Also my contact details should be visible as well.

Requirements
Nice to have
• I have updated the brief with a flyer that I had previously made by a designer. It would be a nice to have if the ad ties in with that. You can also look at my website at www.bravemoor.nu to see what colors I used there.

```html
<!DOCTYPE html>
<html lang="nl">
<head>
<meta charset="utf-8">
<title>Advertentie coachingpraktijk</title>
<link rel="stylesheet" href="https://fonts.googleapis.com/css2?family=Poppins:wght@400;500;600;700;800&display=swap">
<style>
  :root {
    --page: #e9e9e9;
    --paper: #ffffff;
    --ink-grey: #535457;
    --brand-blue: #23527c;
    --coral: #ef6a5c;
    --purple: #6b3fa0;
    --band-blue: #2b5478;
    --navy: #13263f;
    --orange: #f7941d;
    --gold: #c98a12;
    --mint: #cfe9e1;
    --photo-green: #2f6b3a;
    --photo-skin: #a36a4f;
    --white: #ffffff;
  }
  * { box-sizing: border-box; margin: 0; padding: 0; }
  html, body { width: 852px; height: 1200px; overflow: hidden; }
  body { background: var(--page); font-family: "Poppins", sans-serif; position: relative; }

  .ad {
    position: absolute; left: 46px; top: 317px;
    width: 760px; height: 566px;
    background: var(--paper);
    overflow: hidden;
    box-shadow: 6px 8px 10px rgba(0,0,0,0.35);
  }
  .band-blue { position: absolute; left: 0; top: 236px; width: 760px; height: 156px; background: var(--band-blue); }
  .band-navy { position: absolute; left: 0; top: 392px; width: 760px; height: 174px; background: var(--navy); }

  .headline { position: absolute; left: 41px; top: 28px; line-height: 1; }
  .headline .main { font-weight: 800; font-size: 72px; color: var(--ink-grey); letter-spacing: -1px; }
  .headline .line2 { font-weight: 700; font-size: 35px; color: var(--brand-blue); margin-top: 2px; letter-spacing: -0.2px; }
  .headline .line3 { font-weight: 700; font-size: 35px; color: var(--coral); margin-top: 2px; letter-spacing: -0.2px; }
  .headline .amp { color: var(--ink-grey); }

  .intro {
    position: absolute; left: 45px; top: 175px; width: 420px;
    border-left: 3px solid var(--purple); padding-left: 10px;
    font-size: 12.5px; line-height: 1.2; color: var(--ink-grey);
  }

  .banner {
    position: absolute; left: 43px; top: 221px; width: 449px; height: 34px;
    background: var(--coral); border-radius: 4px 0 0 4px;
    color: var(--white); font-weight: 700; font-size: 17.5px;
    padding-left: 19px; line-height: 34px;
  }

  .benefits { position: absolute; left: 42px; top: 272px; list-style: none; }
  .benefits li { display: flex; align-items: center; height: 34px; color: var(--white); font-size: 13.5px; line-height: 1.15; }
  .benefits li + li { margin-top: 0; }
  .benefits .icon {
    flex: none; width: 30px; height: 30px; border-radius: 50%;
    background: var(--orange); box-shadow: -2px 0 0 var(--navy);
    display: flex; align-items: center; justify-content: center; margin-right: 12px;
  }

  .about { position: absolute; left: 49px; top: 411px; width: 370px; font-size: 10.4px; line-height: 1.2; color: var(--white); }

  .contact { position: absolute; left: 50px; top: 488px; color: var(--white); font-weight: 700; font-size: 16px; line-height: 21px; }
  .contact div { display: flex; align-items: center; }
  .contact svg { margin-right: 5px; }

  .name-tag {
    position: absolute; left: 244px; top: 490px; width: 230px; height: 39px;
    background: linear-gradient(100deg, var(--orange) 0 78%, var(--gold) 78% 100%);
    border-radius: 4px 0 0 4px;
    clip-path: polygon(0 0, 92% 0, 100% 100%, 0 100%);
    color: var(--navy); font-weight: 700; font-size: 15.5px; line-height: 39px; padding-left: 12px;
  }

  .mint-arc { position: absolute; left: 472px; top: 166px; width: 492px; height: 492px; border-radius: 50%; background: var(--mint); }
  .portrait {
    position: absolute; left: 436px; top: 176px; width: 512px; height: 512px; border-radius: 50%;
    background: radial-gradient(circle at 42% 42%, var(--photo-skin) 0 22%, #4d3a33 34%, var(--photo-green) 52%, #15361f 80%);
  }

  .brand { position: absolute; left: 520px; top: 32px; width: 220px; text-align: center; }
  .brand .mark { width: 56px; height: 56px; border-radius: 50%; border: 2px solid var(--ink-grey); margin: 0 auto 10px; }
  .brand .name { font-weight: 400; font-size: 34px; color: var(--ink-grey); letter-spacing: 0.5px; }

  .web { position: absolute; left: 505px; top: 501px; font-weight: 500; font-size: 20px; color: var(--white); letter-spacing: 1px; }
  .web span { color: var(--coral); }
</style>
</head>
<body>
  <div class="ad">
    <div class="band-blue"></div>
    <div class="band-navy"></div>

    <div class="mint-arc"></div>
    <div class="portrait" role="img" aria-label="Portretfoto van de coach voor een groene achtergrond"></div>

    <div class="headline">
      <div class="main">COACHING</div>
      <div class="line2">FAMILIEOPSTELLINGEN</div>
      <div class="line3"><span class="amp">&amp;</span> RELATIETHERAPIE</div>
    </div>

    <p class="intro">Trauma’s en negatieve ervaringen vormen ons en blijven nog lang voelbaar. Ze kunnen groei of geluk in de weg staan.</p>

    <div class="banner">Ik ben Amara en ondersteun je bij het:</div>

    <ul class="benefits">
      <li><span class="icon"><svg width="16" height="16" viewBox="0 0 16 16"><circle cx="6" cy="4" r="3" fill="#13263f"/><path d="M1 14c0-4 2-6 5-6s5 2 5 6z" fill="#13263f"/><circle cx="12" cy="12" r="3" fill="none" stroke="#13263f" stroke-width="1.4"/><line x1="10" y1="14" x2="14" y2="10" stroke="#13263f" stroke-width="1.4"/></svg></span>Doorbreken van belemmerende patronen;</li>
      <li><span class="icon"><svg width="16" height="16" viewBox="0 0 16 16"><circle cx="5" cy="5" r="2.5" fill="#13263f"/><circle cx="11" cy="5" r="2.5" fill="#13263f"/><path d="M1 14c0-3 2-5 4-5s4 2 4 5z M7 14c0-3 2-5 4-5s4 2 4 5z" fill="#13263f"/></svg></span>Beter omgaan met conflicten;</li>
      <li><span class="icon"><svg width="16" height="16" viewBox="0 0 16 16"><path d="M8 14L2 8a3.3 3.3 0 0 1 6-4 3.3 3.3 0 0 1 6 4z" fill="#13263f"/><polyline points="3,8 6,8 7,6 9,10 10,8 13,8" fill="none" stroke="#f7941d" stroke-width="1.2"/></svg></span>In gezonde verbinding met elkaar als koppel of<br>met anderen komen;</li>
    </ul>

    <p class="about">Maandelijks geef ik workshops familieopstellingen. Ook houd ik themasessies rond adoptie, moeder-dochterdynamiek of relaties. Ook bied ik individuele coaching, relatietherapie en retraites aan. Kijk op de website voor meer info of neem contact op en ontdek wat het beste bij jou past.</p>

    <div class="contact">
      <div><svg width="12" height="12" viewBox="0 0 12 12"><path d="M2.5 1l2 2-1 1.5a7 7 0 0 0 4 4L9 7.5l2 2-1.5 1.5C5 11 1 7 1 2.5z" fill="#3fbf7f"/></svg>06-12 34 56 78</div>
      <div><svg width="12" height="10" viewBox="0 0 12 10"><rect x="0.5" y="0.5" width="11" height="9" fill="none" stroke="#3fbf7f"/><polyline points="0.5,0.5 6,5.5 11.5,0.5" fill="none" stroke="#3fbf7f"/></svg>info@bravemoor.nu</div>
    </div>

    <div class="name-tag">AMARA VERHOEF</div>

    <div class="brand">
      <div class="mark"></div>
      <div class="name">bravemoor</div>
    </div>

    <div class="web">www.<span>bravemoor</span>.nu</div>
  </div>
</body>
</html>
```